Figure for Manufacture of Wound Healing Gel

Who we are: We are a nationally funded bioengineering laboratory at Harwell Crest University conducting research on the tendon healing properties of a gel manufactured from real tendon.

What we need: We require a figure piece that will be included in an academic publication. With that in mind, the figure must be professional, clear, and concise. A reader would need to glance at the figure for only a moment to understand the process of how we manufacture and store tendon gel. Actual pictures of the in-between steps are included and will need to be cropped to improve the professional look of the design.

The Details: The figure should stepwise show the process of how we manufacture and store tendon gel. In brief, we harvest tendon from donor cadavers. Those tendons undergo decellularization, lyophilization (fancy word for freeze-drying), and are milled into a fine powder. The powder is set in acidified water and treated with digestive enzymes. After 24 hrs, the gel is brought to physiologic pH and salinity and placed in vials. The vials are frozen and again lyophilized (this is so they can be stored and transported easily). Finally the samples are reconstituted with DI water.

The Figure: Should be a linear process (horizontal). The following are the actual steps we wish to include (steps need not be numbered necessarily as long as they are in logical order...

1.) A picture of harvested tendon (Step 1.jpg)
2.) Written description: "Decellularization, lyophilization, and milling"
3.) A picture of milled tendon powder (Step 2.jpg)
4.) Written description: "Digestion with pepsin before establishing physiologic pH and salinity".
5.) A picture of gel (Step 3.jpg)
6.) Written description: "Lyophilization of aliquots"
7.) A picture of freeze-dried gel (Step 4.jpg)
8.) Written description: "Reconstitution with DI water"
9.) A picture of reconstituted gel (Step 5.jpg)

Feel free to message for any questions, comments, or clarifications.

```html
<!DOCTYPE html>
<html lang="en">
<head>
<meta charset="UTF-8">
<title>Manufacture of Tendon Wound Healing Gel</title>
<link rel="stylesheet" href="https://fonts.googleapis.com/css2?family=Crimson+Pro:wght@400&display=swap">
<style>
  :root {
    --bg: #efefef;
    --arrow: #2b3f63;
    --card: #ffffff;
    --card-shadow: #8a8a8a;
    --ink: #1a1a1a;
    --dish-glass: #d9dcde;
    --tendon: #d9cbb0;
    --powder: #e8dcc0;
    --gel: #f2f2ee;
    --vial-cap: #e0561f;
    --vial-body: #dcdcdc;
  }
  html, body {
    margin: 0;
    padding: 0;
    overflow: hidden;
    background: var(--bg);
  }
  .figure {
    position: relative;
    width: 1200px;
    height: 360px;
    overflow: hidden;
    background: var(--bg);
    font-family: "Crimson Pro", "Palatino Linotype", serif;
    color: var(--ink);
  }
  .timeline {
    position: absolute;
    left: 0;
    top: 0;
  }
  .step-photo {
    position: absolute;
  }
  .dish {
    border-radius: 50%;
  }
  .photo-tendon {
    left: 20px; top: 104px; width: 132px; height: 84px;
    background: radial-gradient(ellipse at 50% 45%, var(--tendon) 0%, #cfc6b6 45%, var(--dish-glass) 70%, #c4c7c9 100%);
  }
  .photo-powder {
    left: 280px; top: 100px; width: 152px; height: 88px;
    background: radial-gradient(ellipse at 50% 40%, var(--powder) 0%, #d8cfbd 30%, #4a4a48 55%, var(--dish-glass) 78%, #c0c3c5 100%);
  }
  .photo-gel {
    left: 590px; top: 98px; width: 130px; height: 88px;
    background: radial-gradient(ellipse at 45% 42%, var(--gel) 0%, #dedede 25%, #6a6d70 50%, var(--dish-glass) 75%, #c2c5c7 100%);
  }
  .vial {
    width: 40px; height: 130px;
    border-radius: 6px 6px 12px 12px;
    background: linear-gradient(180deg, var(--vial-cap) 0%, var(--vial-cap) 22%, var(--vial-body) 24%, #f0efec 55%, #d8cfbf 85%, #bdbdbd 100%);
  }
  .photo-dried { left: 894px; top: 56px; }
  .photo-reconstituted {
    left: 1128px; top: 56px;
    background: linear-gradient(180deg, var(--vial-cap) 0%, var(--vial-cap) 22%, var(--vial-body) 24%, #f2f0e8 40%, #e6dfcd 70%, #cfc7b5 100%);
  }
  .step-label {
    position: absolute;
    box-sizing: border-box;
    background: var(--card);
    box-shadow: 4px 4px 0 var(--card-shadow);
    font-size: 13px;
    line-height: 1.45;
    text-align: center;
    padding: 9px 8px;
  }
  .label-decellularization { left: 102px; top: 222px; width: 170px; height: 54px; }
  .label-digestion { left: 422px; top: 226px; width: 142px; height: 90px; }
  .label-lyophilization { left: 718px; top: 226px; width: 174px; height: 94px; }
  .label-reconstitution { left: 990px; top: 226px; width: 134px; height: 52px; }
</style>
</head>
<body>
  <main class="figure">
    <svg class="timeline" width="1200" height="360" viewBox="0 0 1200 360" aria-hidden="true">
      <line x1="34" y1="197" x2="1130" y2="197" stroke="var(--arrow)" stroke-width="5"/>
      <path d="M1112 172 L1158 197 L1112 220 L1124 197 Z" fill="var(--arrow)"/>
    </svg>

    <div class="step-photo dish photo-tendon" role="img" aria-label="Photograph of harvested tendon strands in a glass dish"></div>
    <div class="step-photo dish photo-powder" role="img" aria-label="Photograph of milled tendon powder in a glass dish"></div>
    <div class="step-photo dish photo-gel" role="img" aria-label="Photograph of digested tendon gel in a glass dish"></div>
    <div class="step-photo vial photo-dried" role="img" aria-label="Photograph of freeze-dried gel aliquot in a capped vial"></div>
    <div class="step-photo vial photo-reconstituted" role="img" aria-label="Photograph of reconstituted gel in a capped vial"></div>

    <div class="step-label label-decellularization">Decellularization,<br>lyophilization, and milling</div>
    <div class="step-label label-digestion">Digestion with pepsin before establishing physiologic pH and salinity</div>
    <div class="step-label label-lyophilization">Lyophilization of aliquots<br>Reconstitution with DI water<br>Completed process -<br>reconstituted gel</div>
    <div class="step-label label-reconstitution">Reconstitution with<br>DI water</div>
  </main>
</body>
</html>
```